Realtor resource

This is a website that provides resources for Realtors and their customers (home buyers and sellers).

There are 5 pages that I need redesigned:

1. Homepage: https://brightporchhelp.com/
2. Support Page/Contact Us: https://brightporchhelp.com/contact-us/
3. Agent Dashboard - See attached screenshot
4. Real Estate Documents page - See attached screenshot
5. Real Estate Contract page - see attached screenshot

Target Market(s)

Real estate agents and their customers.

Industry/Entity Type

Real Estate

Number of Pages Required

5+ page

Requirements
Must have
• Please use a modern design and incorporate design with current logo.

```html
<!DOCTYPE html>
<html lang="en">
<head>
<meta charset="utf-8">
<title>BrightPorchHelp – Real Estate Contracts Explained</title>
<link href="https://fonts.googleapis.com/css2?family=Poppins:wght@400;500;600&family=Montserrat:wght@600;700&family=Poiret+One&display=swap" rel="stylesheet">
<style>
  :root {
    --bg: #f5f2f1;
    --ink: #1d1d1f;
    --navy: #243041;
    --orange: #fdaa48;
    --white: #ffffff;
  }
  * { box-sizing: border-box; margin: 0; padding: 0; }
  html, body { width: 1200px; height: 751px; overflow: hidden; }
  body {
    position: relative;
    background: var(--bg);
    font-family: "Poppins", sans-serif;
    color: var(--ink);
  }
  .brand {
    position: absolute; left: 160px; top: 31px;
    font: 600 25px/1 "Poppins", sans-serif;
    color: var(--ink);
    text-decoration: none;
    white-space: nowrap;
  }
  .main-nav {
    position: absolute; left: 453px; top: 38px;
    display: flex; gap: 14px;
    font: 500 11.5px/16px "Poppins", sans-serif;
    letter-spacing: 0.4px;
  }
  .main-nav a { color: var(--ink); text-decoration: none; }
  .main-nav .sep { color: var(--ink); }
  .login-btn {
    position: absolute; left: 939px; top: 31px;
    width: 100px; height: 31px;
    background: var(--orange); color: var(--white);
    font: 500 10.5px/31px "Poppins", sans-serif;
    text-align: center; letter-spacing: 0.4px;
  }
  .hero-title {
    position: absolute; left: 0; top: 190px; width: 1200px;
    text-align: center;
    font: 400 45px/55px "Poiret One", sans-serif;
    letter-spacing: 3px;
    color: var(--ink);
  }
  .hero-byline {
    position: absolute; left: 0; top: 335px; width: 1200px;
    text-align: center;
    font: 700 20px/24px "Montserrat", sans-serif;
    color: var(--orange); letter-spacing: 0.5px;
  }
  .hero-byline small {
    font-size: 11px; color: var(--navy); margin-right: 4px; letter-spacing: 1px;
  }
  .audience-btn {
    position: absolute; top: 432px; width: 187px; height: 40px;
    font: 500 12.5px/40px "Poppins", sans-serif;
    color: var(--white); text-align: center; letter-spacing: 0.6px;
  }
  .audience-btn.realtor { left: 396px; background: var(--orange); }
  .audience-btn.buyers { left: 614px; background: var(--navy); }
  .search-band {
    position: absolute; left: 0; top: 569px; width: 1200px; height: 50px;
    background: var(--navy);
  }
  .search-label {
    position: absolute; left: 238px; top: 17px;
    font: 500 12px/16px "Poppins", sans-serif; color: var(--orange);
  }
  .search-field {
    position: absolute; left: 408px; top: 13px; width: 421px; height: 26px;
    background: var(--white);
    font: 400 9.5px/26px "Poppins", sans-serif; color: #333;
    padding-left: 8px;
  }
  .search-field svg { position: absolute; right: 9px; top: 6px; }
  .advanced-search {
    position: absolute; left: 852px; top: 16px;
    display: flex; align-items: center; gap: 6px;
    font: 500 12px/16px "Poppins", sans-serif; color: var(--orange);
  }
  .signup-band {
    position: absolute; left: 0; top: 619px; width: 1200px; height: 94px;
    background: var(--orange);
  }
  .signup-label {
    position: absolute; left: 313px; top: 39px;
    font: 700 13.5px/18px "Montserrat", sans-serif;
    color: var(--white); letter-spacing: 0.3px;
    white-space: nowrap;
  }
  .signup-field {
    position: absolute; left: 501px; top: 34px; width: 299px; height: 27px;
    background: var(--white);
    font: 400 9.5px/27px "Poppins", sans-serif; color: #333; padding-left: 18px;
  }
  .signup-submit {
    position: absolute; left: 811px; top: 34px; width: 88px; height: 27px;
    border: 1.5px solid var(--white);
    font: 500 9.5px/24px "Poppins", sans-serif; color: var(--white);
    text-align: center; letter-spacing: 0.4px;
  }
  .site-footer {
    position: absolute; left: 0; top: 713px; width: 1200px; height: 38px;
    background: var(--navy);
  }
  .footer-legal {
    position: absolute; left: 163px; top: 12px;
    font: 400 9.5px/14px "Poppins", sans-serif; color: var(--white);
  }
  .footer-legal a { color: var(--white); text-decoration: none; }
  .footer-legal .pipe { margin: 0 8px; }
  .social-links {
    position: absolute; left: 973px; top: 15px; display: flex; gap: 15px;
  }
  .social-links span {
    width: 9px; height: 9px; border-radius: 50%; background: var(--white); display: block;
  }
</style>
</head>
<body>
  <header>
    <a class="brand" href="https://brightporchhelp.com/">BrightPorchHelp</a>
    <nav class="main-nav">
      <a href="https://brightporchhelp.com/">HOME</a><span class="sep">-</span>
      <a href="https://brightporchhelp.com/contact-us/">SUPPORT</a><span class="sep">-</span>
      <a href="#">REAL ESTATE DOCUMENTS</a><span class="sep">-</span>
      <a href="https://brightporchhelp.com/contact-us/">CONTACT</a>
    </nav>
    <div class="login-btn">LOGIN</div>
  </header>

  <main>
    <h1 class="hero-title">REAL ESTATE CONTRACTS<br>EXPLAINED IN PLAIN LANGUAGE</h1>
    <p class="hero-byline"><small>BY</small> TEXAS REAL ESTATE ATTORNEYS.</p>
    <div class="audience-btn realtor">REALTOR</div>
    <div class="audience-btn buyers">BUYERS &amp; SELLERS</div>
  </main>

  <section class="search-band">
    <span class="search-label">Need Help? Search Here</span>
    <div class="search-field">Type your serach&nbsp; keyword here
      <svg width="13" height="13" viewBox="0 0 13 13"><circle cx="5.5" cy="5.5" r="4.2" fill="none" stroke="#243041" stroke-width="1.8"/><line x1="8.6" y1="8.6" x2="12" y2="12" stroke="#243041" stroke-width="2"/></svg>
    </div>
    <span class="advanced-search">
      <svg width="16" height="16" viewBox="0 0 16 16"><g fill="#fdaa48"><circle cx="8" cy="8" r="5.5"/><rect x="6.6" y="0.5" width="2.8" height="15"/><rect x="0.5" y="6.6" width="15" height="2.8"/><rect x="6.6" y="0.5" width="2.8" height="15" transform="rotate(45 8 8)"/><rect x="6.6" y="0.5" width="2.8" height="15" transform="rotate(-45 8 8)"/></g><circle cx="8" cy="8" r="2.2" fill="#243041"/></svg>
      Advanced Search
    </span>
  </section>

  <section class="signup-band">
    <span class="signup-label">SIGN UP FOR UPDATES</span>
    <div class="signup-field">Type your email id</div>
    <div class="signup-submit">SUBMIT</div>
  </section>

  <footer class="site-footer">
    <p class="footer-legal">© Copyright 2019. All Rights Reserved.<span class="pipe">|</span><a href="https://brightporchhelp.com/contact-us/">Contact Us</a></p>
    <div class="social-links"><span></span><span></span><span></span></div>
  </footer>
</body>
</html>
```